Machining Business Order Thank You Insert

I am looking for a business style card to include with orders that I ship. The card needs to thank the recipient for their order, and encourage them to leave a review. The card should include my business name and contact information and have an area to hand write a message.

I mainly sale on Crafvine and my own website. We are a machining an manufacturing business that are in the sale of mostly metal machined and 3d printed plastic products.

The front of the card should include the following:
Logo: (attached)
Snapgrid: https://www.instagram.com/quillforge/
Friendwall: https://www.facebook.com/QuillForge
Website: https://www.quillforge-example.com/

The back of the card needs an area to write a message

Industry/Entity Type

3D Printing, Machining, Crafvine

Contact Information for Business Card

Black or white front, white back to write a personal message

Font styles to use
Sans Serif

Colors

Designer to choose colors to be used in the design.

Requirements
Must have
• Encourage a review, social media info

```html
<!DOCTYPE html>
<html lang="en">
<head>
<meta charset="utf-8">
<title>QuillForge – Thank You Insert</title>
<link rel="stylesheet" href="https://fonts.googleapis.com/css2?family=Barlow:wght@400;500;600&family=Kaushan+Script&family=Open+Sans:wght@400&display=swap">
<style>
  :root {
    --backdrop: #8b8e90;
    --card-white: #ffffff;
    --card-dark-top: #2c2c2c;
    --card-dark-bottom: #1b1b1b;
    --accent: #e8582a;
    --steel: #6f6f71;
    --text-light: #f2f2f2;
    --faint-name: #f3ebe6;
  }
  * { box-sizing: border-box; margin: 0; padding: 0; }
  html, body {
    width: 1200px;
    height: 928px;
    overflow: hidden;
    background: var(--backdrop);
    font-family: "Barlow", sans-serif;
  }
  .canvas { position: relative; width: 1200px; height: 928px; }

  .card { position: absolute; border-radius: 16px; overflow: hidden; }

  /* Message side */
  .card--message {
    left: 267px; top: 59px; width: 670px; height: 383px;
    background: var(--card-white);
    display: flex; align-items: center; justify-content: center;
  }
  .card--message .faint-name {
    font-weight: 500;
    font-size: 64px;
    letter-spacing: 0.3em;
    color: var(--faint-name);
    padding-left: 0.3em;
  }

  /* Thank-you side */
  .card--thanks {
    left: 264px; top: 484px; width: 676px; height: 387px;
    background: linear-gradient(180deg, var(--card-dark-top), var(--card-dark-bottom));
  }
  .brand-mark {
    position: absolute; left: 140px; top: 118px;
    width: 96px; height: 96px;
    border: 5px solid var(--steel);
  }
  .brand-name {
    position: absolute; left: 80px; top: 256px; width: 216px;
    font-weight: 500; font-size: 23px; letter-spacing: 0.3em;
    padding-left: 0.3em;
    color: var(--accent); text-align: center; white-space: nowrap;
  }

  .thanks-word {
    position: absolute;
    font-family: "Kaushan Script", cursive;
    line-height: 1;
    white-space: nowrap;
  }
  .thanks-word--thank { left: 374px; top: 96px; font-size: 72px; color: var(--accent); }
  .thanks-word--you { left: 374px; top: 166px; font-size: 76px; color: var(--steel); }

  .order-word {
    position: absolute;
    font-family: "Open Sans", sans-serif; font-weight: 400;
    color: var(--text-light); line-height: 1;
    transform: rotate(-12deg); transform-origin: left bottom;
    white-space: nowrap;
  }
  .order-word--for { left: 520px; top: 196px; font-size: 32px; }
  .order-word--your-order { left: 406px; top: 264px; font-size: 33px; letter-spacing: 0.02em; }

  .review-bar {
    position: absolute; left: 0; right: 0; top: 334px;
    display: flex; justify-content: center; align-items: center; gap: 12px;
    font-size: 16.5px; color: var(--text-light); white-space: nowrap;
  }
  .review-bar .label { font-weight: 600; }
  .contact { display: flex; align-items: center; gap: 6px; font-weight: 400; letter-spacing: 0.03em; }
  .contact .mark-square { width: 17px; height: 17px; border-radius: 3px; background: var(--accent); }
  .contact svg { display: block; }
</style>
</head>
<body>
<main class="canvas">
  <section class="card card--message" aria-label="Message side of the card">
    <span class="faint-name">QUILLFORGE</span>
  </section>

  <section class="card card--thanks" aria-label="Thank-you side of the card">
    <div class="brand-mark" aria-hidden="true"></div>
    <div class="brand-name">QUILLFORGE</div>

    <span class="thanks-word thanks-word--thank">Thank</span>
    <span class="thanks-word thanks-word--you">You</span>
    <span class="order-word order-word--for">for</span>
    <span class="order-word order-word--your-order">Your Order</span>

    <div class="review-bar">
      <span class="label">Leave A Review:</span>
      <span class="contact"><span class="mark-square"></span>@quillforge</span>
      <span class="contact"><span class="mark-square"></span>@QuillForge</span>
      <span class="contact">
        <svg width="17" height="17" viewBox="0 0 16 16" aria-hidden="true">
          <circle cx="8" cy="8" r="7" fill="none" stroke="var(--accent)" stroke-width="2"/>
          <ellipse cx="8" cy="8" rx="3" ry="7" fill="none" stroke="var(--accent)" stroke-width="1.4"/>
          <line x1="1" y1="8" x2="15" y2="8" stroke="var(--accent)" stroke-width="1.4"/>
        </svg>
        www.quillforge-example.com
      </span>
    </div>
  </section>
</main>
</body>
</html>
```